LoftWren Project

We need a simple corporate website with 3-4 pages total.
We already have the logo and text.
We like the scroll design
we like this look, feel and design http://morvaplex.example

Target Market(s)

The target market is B to B and consumer brands and vendors/distributors

Font styles to use
Serif

Colors
eaf1f7
f5f5f5
ffffff

Requirements
Must have
• Must be a coded website and put in place with wordpress
we like the scroll design

```html
<!DOCTYPE html>
<html lang="en">
<head>
<meta charset="utf-8">
<title>LoftWren</title>
<link href="https://fonts.googleapis.com/css2?family=Arimo:wght@400;700&display=swap" rel="stylesheet">
<style>
:root{
  --brand-blue:#00a0e6;
  --deep-blue:#0b86d4;
  --frame-blue:#4cc0f1;
  --pale-blue:#e1f1f8;
  --brown:#6b3d1e;
  --rust:#7a3418;
  --gold:#e3a532;
  --ink:#333333;
  --grey:#666666;
  --light-grey:#f0f0f0;
  --footer:#1d2125;
  --white:#ffffff;
}
*{margin:0;padding:0;box-sizing:border-box}
html,body{width:1200px;height:2479px;overflow:hidden}
body{font-family:"Arimo",Arial,sans-serif;color:var(--ink);background:var(--white);position:relative}
.abs{position:absolute}

/* header */
.top-rule{left:0;top:0;width:1200px;height:5px;background:var(--brand-blue)}
.brand{left:198px;top:48px;display:flex;align-items:center;gap:10px}
.brand-mark{width:26px;height:26px;background:var(--brand-blue)}
.brand-name{font-size:34px;font-weight:700;color:var(--brown);letter-spacing:1px}
.search{left:848px;top:15px;width:152px;height:27px;border:1px solid #cfcfcf;font-size:11px;color:#888;padding:7px 12px}
.search svg{position:absolute;right:9px;top:7px}
.nav{top:82px;left:0;width:1200px;height:52px}
.nav a{position:absolute;font-size:11px;font-weight:700;color:var(--brand-blue);text-decoration:none;transform:translateX(-50%);top:0}
.nav a.active{color:var(--brown)}
.nav-indicator{left:552px;top:127px;width:69px;height:7px;background:var(--brand-blue)}
.header-shadow{left:0;top:132px;width:1200px;height:2px;background:#dcdcdc}

/* hero */
.hero{left:0;top:134px;width:1200px;height:471px;background:linear-gradient(100deg,#e9eef2 0%,#b8c9d3 30%,#d3dde3 55%,#5e6a6e 80%,#3d4440 100%)}
.hero-arrow{top:344px}
.hero-dots{left:575px;top:580px;display:flex;gap:4px}
.dot{width:11px;height:11px;border-radius:50%;border:1px solid #888;background:var(--white)}
.dot.on{background:#5d7b8c}

/* brand band */
.band{left:0;top:605px;width:1200px;height:89px;background:var(--brand-blue)}
.band-title{left:271px;top:624px;font-size:23px;font-weight:700;color:var(--white);line-height:29px}
.band-brace{left:418px;top:614px}
.band-text{left:493px;top:624px;font-size:18px;color:#3d4a55;line-height:23px;width:340px}
.band-btn{left:853px;top:628px;width:107px;height:40px;background:var(--brown);color:var(--white);font-size:14px;display:flex;align-items:center;justify-content:center;box-shadow:0 2px 3px rgba(0,0,0,.3)}

/* welcome */
.welcome-title{left:0;top:710px;width:1200px;text-align:center;font-size:28px;color:var(--brand-blue)}
.welcome-copy{left:198px;top:757px;width:802px;text-align:center;font-size:9.5px;line-height:14px;color:var(--grey)}
.welcome-shadow{left:676px;top:850px;width:338px;height:264px;background:var(--light-grey)}
.welcome-photo{left:200px;top:833px;width:800px;height:251px;background:linear-gradient(100deg,#f4f4f4 0%,#dfe0e2 30%,#6c7480 50%,#e2d5cc 70%,#f3f3f3 100%)}

/* services */
.services{left:0;top:1121px;width:1200px;height:481px;background:var(--brand-blue)}
.services-title{left:0;top:1146px;width:1200px;text-align:center;font-size:27px;color:var(--white);text-shadow:0 1px 2px rgba(0,0,0,.25)}
.service{width:243px}
.service-frame{height:139px;background:var(--frame-blue);padding:11px;box-shadow:0 4px 6px rgba(0,60,100,.35)}
.service-photo{width:100%;height:100%}
.service-label{text-align:center;font-size:18px;font-weight:700;color:var(--white);margin-top:20px}

/* people */
.people-title{left:0;top:1630px;width:1200px;text-align:center;font-size:27px;color:#5a5a5a}
.people{left:0;top:1683px;width:1200px;height:296px;background:var(--pale-blue)}
.person{width:285px;height:129px;background:var(--deep-blue)}
.person-quote{position:absolute;left:66px;top:20px;width:200px;font-size:9px;line-height:13px;color:var(--white)}
.person-quote::before,.person-quote::after{position:absolute;color:var(--gold);font-size:15px}
.person-quote::before{content:"\201C";left:-12px;top:-8px}
.person-quote::after{content:"\201D";left:60px;bottom:-16px}
.person-role{position:absolute;right:34px;bottom:11px;font-size:8px;color:#0a1a2a}
.avatar{width:86px;height:86px;border-radius:50%;background:var(--gold);padding:7px}
.avatar span{display:block;width:100%;height:100%;border-radius:50%;background:linear-gradient(160deg,#cfd6dc,#8a939b)}

/* testimonials */
.testimonials{left:0;top:1980px;width:1200px;height:227px;background:linear-gradient(90deg,#b9d6e6 0%,#c4cfd3 40%,#cbb9ac 60%,#a8c6d6 85%,#8da0a8 100%)}
.testimonials-title{left:0;top:1995px;width:1200px;text-align:center;font-size:22px;color:var(--white)}
.testimonial-box{left:200px;top:2075px;width:802px;height:100px;background:var(--deep-blue);padding:36px 30px 0;text-align:center;font-size:14.5px;line-height:16px;color:var(--white)}
.testimonial-avatar{left:545px;top:2042px;width:64px;height:64px;border-radius:50%;background:var(--white);padding:3px}
.testimonial-avatar span{display:block;width:100%;height:100%;border-radius:50%;background:linear-gradient(160deg,#d7d7d7,#7d858b)}
.testimonial-dots{left:553px;top:2184px;display:flex;gap:3px}
.testimonial-dots .dot{width:13px;height:13px;border-color:#2b6e96}
.testimonial-dots .dot.on{background:var(--deep-blue)}

/* quote */
.quote-title{left:200px;top:2251px;font-size:24px;font-weight:700;color:#111}
.quote-sub{left:210px;top:2287px;font-size:13px;color:#111}
.quote-arrow{left:306px;top:2303px}
.quote-form{left:402px;top:2250px;width:596px;height:69px;border:2px solid #d0d0d0;box-shadow:0 1px 3px rgba(0,0,0,.15)}
.quote-input{position:absolute;left:22px;top:27px;font-size:11px;color:#444}
.quote-btn{position:absolute;right:-2px;top:-2px;width:201px;height:69px;background:var(--rust);color:var(--white);font-size:14px;font-weight:700;display:flex;align-items:center;justify-content:center}

/* footer */
.footer-rule{left:0;top:2364px;width:1200px;height:9px;background:var(--deep-blue)}
.footer{left:0;top:2373px;width:1200px;height:106px;background:var(--footer)}
.footer-links{left:200px;top:2402px;font-size:10px;color:var(--white)}
.footer-links span{margin:0 5px;color:#aaa}
.footer-copy{left:200px;top:2430px;font-size:9.5px;color:#ddd}
.social{top:2402px;display:flex;gap:7px;left:897px}
.social i{width:30px;height:30px;border-radius:50%;background:#dcdcdc;display:block}
</style>
</head>
<body>

<header>
  <div class="abs top-rule"></div>
  <div class="abs brand"><span class="brand-mark"></span><span class="brand-name">LoftWren</span></div>
  <div class="abs search">Search
    <svg width="12" height="12" viewBox="0 0 12 12"><circle cx="5" cy="5" r="3.6" fill="none" stroke="#0b86d4" stroke-width="1.6"/><line x1="7.6" y1="7.6" x2="11" y2="11" stroke="#0b86d4" stroke-width="1.8"/></svg>
  </div>
  <nav class="abs nav">
    <a class="active" style="left:583px">Home</a>
    <a style="left:655px">About Us</a>
    <a style="left:734px">Services</a>
    <a style="left:812px">Our Team</a>
    <a style="left:891px">Projects</a>
    <a style="left:972px">Contact Us</a>
  </nav>
  <div class="abs header-shadow"></div>
  <div class="abs nav-indicator"></div>
</header>

<section>
  <div class="abs hero" role="img" aria-label="Smiling shopper handing a card to a cashier at a boutique till"></div>
  <svg class="abs hero-arrow" style="left:64px" width="20" height="30" viewBox="0 0 20 30"><path d="M16 2 L4 15 L16 28" fill="none" stroke="#3f8fc4" stroke-width="5"/></svg>
  <svg class="abs hero-arrow" style="left:1110px" width="20" height="30" viewBox="0 0 20 30"><path d="M4 2 L16 15 L4 28" fill="none" stroke="#3f8fc4" stroke-width="5"/></svg>
  <div class="abs hero-dots"><span class="dot on"></span><span class="dot"></span><span class="dot"></span></div>
</section>

<section>
  <div class="abs band"></div>
  <div class="abs band-title">Brand<br>Running</div>
  <svg class="abs band-brace" width="48" height="72" viewBox="0 0 48 72"><path d="M6 3 C24 3 22 20 24 30 C26 34 32 36 44 36 C32 36 26 38 24 42 C22 52 24 69 6 69" fill="none" stroke="#6b3d1e" stroke-width="4"/></svg>
  <div class="abs band-text">Nulla convallis egestas rhoncus. Donec facilisis fermentum sem</div>
  <div class="abs band-btn">Click here</div>
</section>

<section>
  <h1 class="abs welcome-title" style="font-weight:400">Welcome LOFTWREN</h1>
  <p class="abs welcome-copy">Lorem ipsum dolor sit amet, consectetur adipiscing elit. Nulla convallis egestas rhoncus. Donec facilisis fermentum sem, ac viverra ante luctus vel. Donec vel mauris quam. Aliquam pellentesque pellentesque turpis, ut bibendum sapien sollicitudin nec. Pellentesque posuere ornare placerat. Suspendisse potenti. Quisque massa tortor, tristique non tristique at, luctus sed massa. Donec libero eros, mollis ac...Lorem ipsum dolor sit amet, consectetur adipiscing elit. Nulla convallis egestas rhoncus. Donec facilisis fermentum sem, ac viverra ante luctus vel. Donec vel mauris quam. Aliquam pellentesque pellentesque turpis, ut bibendum sapien sollicitudin nec</p>
  <div class="abs welcome-shadow"></div>
  <div class="abs welcome-photo" role="img" aria-label="Hand holding a payment card against a bright white background"></div>
</section>

<section>
  <div class="abs services"></div>
  <h2 class="abs services-title" style="font-weight:400">Services</h2>
  <div class="abs service" style="left:200px;top:1203px"><div class="service-frame"><div class="service-photo" role="img" aria-label="Keyboard key with a shopping cart symbol" style="background:linear-gradient(135deg,#1c2f6e,#6f8fd6 50%,#1a2a5c)"></div></div><div class="service-label">E commerce</div></div>
  <div class="abs service" style="left:479px;top:1203px"><div class="service-frame"><div class="service-photo" role="img" aria-label="Shopper paying with a card at a clothing store counter" style="background:linear-gradient(135deg,#d9c6b4,#c6483c 50%,#8bb04a)"></div></div><div class="service-label">Retail shopping</div></div>
  <div class="abs service" style="left:755px;top:1203px"><div class="service-frame"><div class="service-photo" role="img" aria-label="Cashier serving a customer at a supermarket checkout" style="background:linear-gradient(135deg,#d7dde0,#7a3b2c 55%,#e9ecee)"></div></div><div class="service-label">Retail</div></div>
  <div class="abs service" style="left:200px;top:1397px"><div class="service-frame"><div class="service-photo" role="img" aria-label="Wall of stacked vintage storage boxes" style="background:linear-gradient(135deg,#3a3a30,#7e7458 50%,#2f3a44)"></div></div><div class="service-label">Shopping</div></div>
  <div class="abs service" style="left:479px;top:1397px"><div class="service-frame"><div class="service-photo" role="img" aria-label="Business people reviewing papers at a laptop" style="background:linear-gradient(135deg,#f2f2f2,#9aa0a8 50%,#2d3138)"></div></div><div class="service-label">Sales</div></div>
  <div class="abs service" style="left:755px;top:1397px"><div class="service-frame"><div class="service-photo" role="img" aria-label="Woman stretching her arms on a sunny beach" style="background:linear-gradient(180deg,#4d8ed0,#a9cdec 60%,#e4ddcf)"></div></div><div class="service-label">Know more</div></div>
</section>

<section>
  <h2 class="abs people-title" style="font-weight:400">Our People</h2>
  <div class="abs people"></div>
  <div class="abs person" style="left:276px;top:1696px"><p class="person-quote">Lorem ipsum dolor sit amet, consectetur adipiscing elit. Nulla convallis egestas rhoncus. Donec facilisis fermentum sem, ac viverra ante luctus vel. Donec vel mauris quam.</p><span class="person-role">-SEO John</span></div>
  <div class="abs person" style="left:669px;top:1696px"><p class="person-quote">Lorem ipsum dolor sit amet, consectetur adipiscing elit. Nulla convallis egestas rhoncus. Donec facilisis fermentum sem, ac viverra ante luctus vel. Donec vel mauris quam.</p><span class="person-role">-SEO John</span></div>
  <div class="abs person" style="left:276px;top:1835px"><p class="person-quote">Lorem ipsum dolor sit amet, consectetur adipiscing elit. Nulla convallis egestas rhoncus. Donec facilisis fermentum sem, ac viverra ante luctus vel. Donec vel mauris quam.</p><span class="person-role">-SEO John</span></div>
  <div class="abs person" style="left:669px;top:1835px"><p class="person-quote">Lorem ipsum dolor sit amet, consectetur adipiscing elit. Nulla convallis egestas rhoncus. Donec facilisis fermentum sem, ac viverra ante luctus vel. Donec vel mauris quam.</p><span class="person-role">-SEO John</span></div>
  <div class="abs avatar" style="left:246px;top:1718px"><span role="img" aria-label="Team member portrait"></span></div>
  <div class="abs avatar" style="left:639px;top:1718px"><span role="img" aria-label="Team member portrait"></span></div>
  <div class="abs avatar" style="left:246px;top:1857px"><span role="img" aria-label="Team member portrait"></span></div>
  <div class="abs avatar" style="left:639px;top:1857px"><span role="img" aria-label="Team member portrait"></span></div>
</section>

<section>
  <div class="abs testimonials" role="img" aria-label="Soft blurred background of a person in an office"></div>
  <h2 class="abs testimonials-title" style="font-weight:400">Testmonials</h2>
  <div class="abs testimonial-box">" Nulla facilisi. Quisque a nibh arcu, vel hendrerit eros. Sed augue metus, semper non elementum nec, feugiat non justo. Duis orci erat, aliquam id vulputate sit amet, egestas ac tellus. Cras a mi massa. Sed convallis massa eget metus...</div>
  <div class="abs testimonial-avatar"><span role="img" aria-label="Client portrait"></span></div>
  <div class="abs testimonial-dots"><span class="dot on"></span><span class="dot"></span><span class="dot"></span></div>
</section>

<section>
  <div class="abs quote-title">Try us now!</div>
  <div class="abs quote-sub">Get a free quote!</div>
  <svg class="abs quote-arrow" width="80" height="26" viewBox="0 0 80 26"><path d="M2 14 C20 24 50 22 70 12" fill="none" stroke="#444" stroke-width="1.2"/><path d="M62 9 L71 11 L66 18" fill="none" stroke="#444" stroke-width="1.2"/></svg>
  <div class="abs quote-form"><span class="quote-input">What are you looking for?</span><div class="quote-btn">Get quote now</div></div>
</section>

<footer>
  <div class="abs footer-rule"></div>
  <div class="abs footer"></div>
  <div class="abs footer-links">Home<span>|</span>About us<span>|</span>Counselling<span>|</span>Workshop<span>|</span>Contact us</div>
  <div class="abs footer-copy">Content copyright 2014. LoftWren. All rights reserved.</div>
  <div class="abs social"><i></i><i></i><i></i></div>
</footer>

</body>
</html>
```